Tall Willow Sticker Design for TRIM 9

ur business name is ' Tall Willow ' ( Logo attached ).
The Product is called ' Trim 9 ' It has six ingredients that need to be listed on the sticker - Chia, Turmeric, Ginger, Dandelion, Macha and Seaweed.
120 capsules in a packet.
I would like it to say the product is a ' Weight loss alternative ' ' all organic ingredients ' All natural '

The logo.

Target Market(s)

Everyone.

Industry/Entity Type

Health And Wellness

Requirements
Must have
• ur business name is ' Tall Willow ' ( Logo attached ).
• The Product is called ' Trim 9 ' It has six ingredients that need to be listed on the sticker - Chia, Turmeric, Ginger, Dandelion, Macha and Seaweed.
• 120 capsules in a packet.
• I would like it to say the product is a ' Weight loss alternative ' ' all organic ingredients ' All natural '
• The logo.
Nice to have
• A catchy image symbolising nature.

```html
<!DOCTYPE html>
<html lang="en">
<head>
<meta charset="utf-8">
<title>Tall Willow – Trim 9 Label</title>
<link href="https://fonts.googleapis.com/css2?family=Pacifico&family=Dancing+Script:wght@700&family=Roboto:wght@400;500;700&display=swap" rel="stylesheet">
<style>
  :root {
    --stage: #e6e7e8;
    --label: #ffffff;
    --logo-tab: #111111;
    --logo-text: #ffffff;
    --title-teal: #3fbfae;
    --ingredient-green: #1f5a2e;
    --capsule-orange: #e0824a;
    --badge-teal-a: #2fc6c0;
    --badge-teal-b: #d7b95a;
    --badge-pink-a: #f29a5c;
    --badge-pink-b: #ee6fa8;
    --forest-deep: #2f7a2a;
    --forest-light: #7fc24a;
    --water: #9fd8de;
    --sky: #e9f2f3;
  }
  * { margin: 0; padding: 0; box-sizing: border-box; }
  html, body { width: 1200px; height: 1200px; overflow: hidden; }
  body {
    background: var(--stage);
    font-family: "Roboto", Arial, sans-serif;
    position: relative;
  }
  .label {
    position: absolute;
    left: 80px; top: 240px;
    width: 1040px; height: 720px;
    background: var(--label);
    overflow: hidden;
    box-shadow: 0 10px 30px rgba(0,0,0,0.12);
  }
  .nature-scene {
    position: absolute;
    left: 0; right: 0; top: 250px; bottom: 0;
    background:
      radial-gradient(ellipse at 30% 70%, rgba(255,255,255,0.55) 0 8%, transparent 20%),
      linear-gradient(90deg, var(--forest-deep) 0%, var(--forest-light) 30%, var(--forest-deep) 55%, var(--water) 75%, var(--sky) 100%);
    -webkit-mask-image: linear-gradient(180deg, transparent 0%, #000 22%, #000 70%, transparent 100%);
    mask-image: linear-gradient(180deg, transparent 0%, #000 22%, #000 70%, transparent 100%);
  }
  .brand-tab {
    position: absolute;
    left: 50%; top: 0;
    transform: translateX(-50%);
    width: 230px; height: 110px;
  }
  .brand-tab svg { position: absolute; inset: 0; }
  .brand-name {
    position: absolute;
    inset: 0 0 22px 0;
    display: flex; align-items: center; justify-content: center; gap: 10px;
    color: var(--logo-text);
    font-family: "Roboto", Arial, sans-serif;
    font-weight: 500;
    font-size: 26px;
  }
  .brand-dot {
    width: 12px; height: 12px; border-radius: 50%;
    background: var(--logo-text);
  }
  .product-title {
    position: absolute;
    left: 0; right: 0; top: 100px;
    text-align: center;
    font-family: "Pacifico", cursive;
    font-size: 150px;
    line-height: 1.1;
    color: var(--title-teal);
  }
  .claims {
    position: absolute;
    left: 0; right: 0; top: 330px;
    display: flex; justify-content: center; gap: 0;
  }
  .claim {
    width: 160px; height: 160px; border-radius: 50%;
    display: flex; align-items: center; justify-content: center;
    text-align: center;
    font-family: "Dancing Script", cursive;
    font-weight: 700;
    font-size: 26px; line-height: 1.05;
    color: #ffffff;
    margin: 0 -6px;
    box-shadow: 0 4px 10px rgba(0,0,0,0.15);
  }
  .claim--organic { background: linear-gradient(135deg, var(--badge-teal-a), var(--badge-teal-b)); margin-top: 40px; }
  .claim--weight { background: linear-gradient(135deg, var(--badge-pink-a), var(--badge-pink-b)); margin-top: 10px; }
  .claim--natural { background: linear-gradient(135deg, var(--badge-teal-a), var(--badge-teal-b)); margin-top: -10px; width: 140px; height: 140px; }
  .ingredients {
    position: absolute;
    left: 0; right: 0; top: 560px;
    text-align: center;
    color: var(--ingredient-green);
    font-weight: 500;
    font-size: 20px;
    letter-spacing: 0.5px;
    line-height: 1.3;
  }
  .capsule-count {
    position: absolute;
    left: 0; right: 0; top: 640px;
    text-align: center;
    color: var(--capsule-orange);
    font-weight: 700;
    font-size: 28px;
  }
</style>
</head>
<body>
  <main class="label">
    <div class="nature-scene" role="img" aria-label="Photo of a waterfall in a green forest flowing into a calm turquoise lake"></div>

    <div class="brand-tab">
      <svg width="230" height="110" viewBox="0 0 230 110" aria-hidden="true">
        <path d="M0 0 H230 V78 L205 100 H25 L0 78 Z" fill="var(--logo-tab)"/>
      </svg>
      <div class="brand-name"><span class="brand-dot"></span>Tall Willow</div>
    </div>

    <h1 class="product-title">Trim9</h1>

    <div class="claims">
      <div class="claim claim--organic">All Organic<br>Ingredients</div>
      <div class="claim claim--weight">Weight Loss<br>Alternative</div>
      <div class="claim claim--natural">All<br>Natural</div>
    </div>

    <p class="ingredients">INGREDIENTS:<br>CHIA, TURMERIC, GINGER, DANDELION, MACHA, SEAWEED</p>
    <p class="capsule-count">120 Capsules</p>
  </main>
</body>
</html>
```